Business Card Design Project

This is a new division in our company. "Meridale Wellsite & Safety" This is a Oilfield Safety company. I have included our new logo. I also have given our other business card. We love double sided with lots of color. We like to stand out. Please DO NOT duplicate our other card and bring your design into it. See all attached files.
Reason: forgot to change this when I posted it.
Here is the correct information card.
www.meridalewellsitesafety.com
Dwayne@meridalewellsitesafety.com
Reason: revision for a few.
Reason: was traveling and need to review designs.
Oil and Gas industry. Masculine look.
Business

```html
<!DOCTYPE html>
<html lang="en">
<head>
<meta charset="utf-8">
<title>Meridale Wellsite &amp; Safety – Business Card</title>
<link rel="stylesheet" href="https://fonts.googleapis.com/css2?family=Open+Sans:wght@400;600;700;800&display=swap">
<style>
  :root {
    --page-bg: #e9e9e9;
    --label: #ee7a55;
    --card-dark: #242424;
    --orange-light: #f27b55;
    --orange-deep: #ee5a2a;
    --brand-teal: #62d3d2;
    --brand-accent: #ee3b2a;
    --divider: #2a2a2a;
    --white: #ffffff;
    --watermark: rgba(160, 50, 20, 0.16);
  }
  * { box-sizing: border-box; margin: 0; padding: 0; }
  html, body {
    width: 1200px;
    height: 1000px;
    overflow: hidden;
  }
  body {
    background: var(--page-bg);
    font-family: "Open Sans", Arial, sans-serif;
    position: relative;
  }
  .side-label {
    position: absolute;
    left: 0;
    width: 1200px;
    text-align: center;
    font-weight: 700;
    font-size: 30px;
    letter-spacing: 1.5px;
    color: var(--label);
  }
  .side-label--front { top: 70px; }
  .side-label--back { top: 500px; }

  .card {
    position: absolute;
    left: 300px;
    width: 600px;
    height: 343px;
    overflow: hidden;
    box-shadow: 0 18px 40px rgba(0,0,0,0.22);
  }
  .card--front { top: 120px; }
  .card--back {
    top: 550px;
    background: linear-gradient(180deg, var(--orange-light) 0%, var(--orange-deep) 100%);
  }

  /* Front */
  .brand-band {
    position: absolute;
    left: 0; top: 0;
    width: 600px;
    height: 162px;
    background: var(--card-dark);
  }
  .brand-lockup {
    position: absolute;
    left: 56px;
    top: 38px;
    display: flex;
    align-items: center;
    gap: 16px;
  }
  .brand-mark {
    width: 22px;
    height: 22px;
    background: var(--brand-accent);
  }
  .brand-name {
    color: var(--brand-teal);
    font-weight: 800;
    line-height: 1;
  }
  .brand-name__main { display: block; font-size: 60px; letter-spacing: 1px; }
  .brand-name__sub { display: block; font-size: 24px; letter-spacing: 2px; margin-top: 6px; }

  .info-band {
    position: absolute;
    left: 0; top: 162px;
    width: 600px;
    height: 181px;
    background: linear-gradient(100deg, var(--orange-light) 0%, var(--orange-deep) 100%);
  }
  .info-divider {
    position: absolute;
    left: 288px;
    top: 0;
    width: 3px;
    height: 181px;
    background: var(--divider);
  }
  .contact-list {
    position: absolute;
    left: 28px;
    top: 24px;
    width: 252px;
    list-style: none;
    color: var(--white);
    font-size: 10.5px;
    line-height: 16px;
    white-space: nowrap;
  }
  .company-details {
    position: absolute;
    left: 304px;
    right: 12px;
    bottom: 36px;
    color: var(--white);
    font-weight: 600;
    white-space: nowrap;
  }
  .company-details__address { font-size: 12px; line-height: 18px; }
  .company-details__web { font-size: 15px; font-weight: 700; line-height: 21px; }

  /* Back */
  .back-watermark {
    position: absolute;
    left: 70px;
    top: 92px;
    color: var(--watermark);
    font-weight: 800;
    line-height: 1;
  }
  .back-watermark__main { display: block; font-size: 80px; letter-spacing: 1px; }
  .back-watermark__sub { display: block; font-size: 32px; letter-spacing: 3px; margin-top: 8px; }
</style>
</head>
<body>
  <div class="side-label side-label--front">Front</div>

  <section class="card card--front" aria-label="Business card front">
    <div class="brand-band">
      <div class="brand-lockup">
        <span class="brand-mark" aria-hidden="true"></span>
        <div class="brand-name">
          <span class="brand-name__main">MERIDALE</span>
          <span class="brand-name__sub">WELLSITE &amp; SAFETY</span>
        </div>
      </div>
    </div>
    <div class="info-band">
      <div class="info-divider"></div>
      <ul class="contact-list">
        <li>Dwayne Kessler</li>
        <li>Office : 281-555-0142</li>
        <li>Cell: 713-555-0187</li>
        <li>Email : Dwayne@meridalewellsitesafety.com</li>
      </ul>
      <div class="company-details">
        <p class="company-details__address">8912 N. Ridgeway Blvd-Carlow,TX 77390</p>
        <p class="company-details__web">www.meridalewellsitesafety.com</p>
      </div>
    </div>
  </section>

  <div class="side-label side-label--back">Back</div>

  <section class="card card--back" aria-label="Business card back">
    <div class="back-watermark" aria-hidden="true">
      <span class="back-watermark__main">MERIDALE</span>
      <span class="back-watermark__sub">WELLSITE &amp; SAFETY</span>
    </div>
  </section>
</body>
</html>
```